Ductless Mini Split Business Website

Amber Kite Services is looking to design an eye catching educational website about installing Ductless mini splits.

Similar to this company.
https://www.cedarcoolair.com/

```html
<!DOCTYPE html>
<html lang="en">
<head>
<meta charset="utf-8">
<title>Amber Kite Services – Ductless Experts</title>
<link href="https://fonts.googleapis.com/css2?family=Lato:wght@400;700;900&display=swap" rel="stylesheet">
<style>
:root{
  --yellow:#ffe000;
  --yellow-deep:#f2d200;
  --ink:#111111;
  --text:#2a2a2a;
  --gray-bg:#ebebeb;
  --card-gray:#a9a9a9;
  --white:#ffffff;
  --footer:#0d0d0d;
}
html,body{margin:0;padding:0;overflow:hidden;}
body{font-family:"Lato",sans-serif;color:var(--text);background:var(--white);}
.page{position:relative;width:1200px;height:4766px;overflow:hidden;background:var(--gray-bg);}
.abs{position:absolute;}
.fill{position:absolute;left:0;top:0;}

/* header */
.header{position:absolute;left:0;top:0;width:1200px;height:130px;background:var(--white);}
.brand{position:absolute;left:50px;top:30px;display:flex;align-items:center;gap:10px;}
.brand-dot{width:34px;height:34px;border-radius:50%;background:var(--yellow);}
.brand-name{font-weight:900;font-size:20px;color:var(--ink);line-height:1.1;}
.brand-tag{position:absolute;left:57px;top:94px;font-weight:900;font-size:17px;color:var(--ink);letter-spacing:.5px;}
.call{position:absolute;right:48px;top:22px;font-size:24px;font-weight:700;color:var(--ink);}
.call span{color:var(--yellow-deep);font-weight:400;}
.nav{position:absolute;right:48px;top:78px;display:flex;gap:30px;font-size:13px;color:var(--ink);}
.nav .active{border-bottom:3px solid var(--yellow);padding-bottom:4px;}

/* hero */
.hero-photo{position:absolute;left:0;top:130px;width:1200px;height:520px;background:linear-gradient(180deg,#9e9e9e 0%,#c6c6c6 55%,#b5a992 100%);}
.hero-title{position:absolute;left:0;width:1184px;text-align:center;}
.hero-go{top:150px;font-weight:900;font-size:50px;color:var(--yellow);}
.hero-l2{top:208px;font-size:40px;color:#222;}
.hero-l3{top:254px;font-size:40px;color:#222;}
.hero-l2 small,.hero-l3 small{font-size:24px;color:var(--yellow);}
.video{position:absolute;left:55px;top:555px;width:540px;height:347px;background:linear-gradient(135deg,#e5edf3,#b8c7d3);}
.video-label{left:89px;top:945px;font-weight:900;font-size:29px;color:var(--ink);}
.intro-title{left:642px;top:712px;font-weight:900;font-size:29px;color:var(--ink);}
.intro-sub{left:642px;top:756px;font-size:16px;line-height:19px;color:var(--ink);}
.intro-text{left:642px;top:808px;width:505px;font-size:12px;line-height:16.4px;color:var(--ink);}
.btn-dark{position:absolute;background:var(--ink);color:var(--white);border-radius:20px;text-align:center;font-weight:700;}
.load{left:642px;top:925px;width:124px;height:34px;line-height:34px;font-size:13px;}

/* help */
.section-head{position:absolute;left:0;width:1200px;text-align:center;font-weight:900;font-size:28px;color:var(--ink);}
.card{position:absolute;width:344px;height:362px;}
.card-img{position:absolute;left:0;top:0;width:100%;height:281px;}
.card-cap{position:absolute;left:0;top:281px;width:100%;height:81px;line-height:81px;text-align:center;font-size:13px;color:var(--white);background:var(--card-gray);}
.card-cap.on{background:var(--yellow);color:var(--ink);}

/* contact */
.h-line{position:absolute;height:4px;background:var(--yellow-deep);}
.block-title{font-weight:900;font-size:28px;color:var(--ink);line-height:35px;}
.field{position:absolute;background:var(--white);border-radius:4px;font-size:12px;color:#777;padding:15px 0 0 20px;box-sizing:border-box;}
.why-item{position:absolute;left:736px;width:420px;}
.why-item svg{position:absolute;left:0;top:0;}
.why-text{position:absolute;left:86px;font-size:12px;line-height:16px;color:#333;}
.why-text b{display:block;font-size:17px;font-weight:400;color:var(--ink);line-height:21px;margin-bottom:2px;}

.quote-mark{position:absolute;font-weight:900;font-size:220px;line-height:1;color:var(--yellow-deep);}

/* more */
.more-card{position:absolute;width:346px;height:354px;}
.more-img{position:absolute;left:0;top:0;width:100%;height:211px;}
.more-body{position:absolute;left:0;top:211px;width:100%;height:143px;text-align:center;}
.more-title{position:absolute;left:0;width:100%;top:36px;font-size:23px;}
.more-btn{position:absolute;left:57px;top:76px;width:232px;height:40px;line-height:40px;border-radius:20px;font-weight:700;font-size:17px;}

/* footer */
.footer{position:absolute;left:0;top:4388px;width:1200px;height:378px;background:var(--footer);color:var(--white);}
.foot-strip{position:absolute;left:0;top:357px;width:1200px;height:21px;background:var(--yellow);}
.foot-title{position:absolute;font-size:19px;font-weight:700;}
.foot-addr{position:absolute;font-size:12px;line-height:15px;}
.map{position:absolute;background:linear-gradient(135deg,#f4f4f4,#dcdcdc);}
.quick{position:absolute;right:48px;text-align:right;font-size:12px;}
.social{position:absolute;top:4627px;width:36px;height:36px;border-radius:50%;background:var(--white);}
</style>
</head>
<body>
<div class="page">

  <!-- Header -->
  <header class="header">
    <div class="brand"><div class="brand-dot"></div><div class="brand-name">Amber Kite<br>Services</div></div>
    <div class="brand-tag">DUCTLESS EXPERTS</div>
    <div class="call"><span>Call Us</span> Now 500-555-0182</div>
    <nav class="nav">
      <span class="active">Home</span><span>About us</span><span>Ductless Heat Pumps</span><span>Ductless Heat Pumps FAQ</span><span>Reviews</span><span>Financing</span><span>Contact us</span>
    </nav>
  </header>

  <!-- Hero -->
  <div class="hero-photo" role="img" aria-label="Bright living room with a grey sofa, yellow cushions and a wall-mounted ductless unit"></div>
  <div class="hero-title hero-go">GO DUCTLESS</div>
  <div class="hero-title hero-l2">Cool&amp; Heat <small>at a</small></div>
  <div class="hero-title hero-l3"><small>Fraction of The</small> COST</div>

  <svg class="fill" width="1200" height="1140" aria-hidden="true">
    <polygon points="0,600 1200,545 1200,1000 295,1128 0,1012" fill="#ffe000"/>
  </svg>

  <div class="video" role="img" aria-label="Technician installing an indoor ductless unit on a wall"></div>
  <svg class="abs" style="left:259px;top:669px" width="130" height="130" aria-hidden="true">
    <circle cx="65" cy="65" r="58" fill="none" stroke="#fff" stroke-width="9"/>
    <polygon points="50,38 50,92 94,65" fill="#fff"/>
  </svg>
  <div class="abs video-label">CASCADE DUCTLESS TIMELAPSE</div>

  <div class="abs intro-title">CASCADE DUCTLESS CREW</div>
  <div class="abs intro-sub">HELPING PORTLAND &amp; SURROUNDING<br>AREAS GO DUCTLESS</div>
  <div class="abs intro-text">Experience maximum comfort, better indoor air quality, and lower utility bills by installing ductless heat pumps in your home. As the premier company for everything ductless-related, Cascade Ductless Crew offers a wide selection of quality ductless systems from industry-leading manufacturers such as Hollis and Kenrow. We are also the experts when it comes to unparalleled ductless solutions. Whether you need repairs or maintenance for an existing unit or are considering switching your base-board heating with a ductless heat pump, our trained technicians can do it all.</div>
  <div class="btn-dark load">LOAD MORE</div>

  <!-- How can we help -->
  <div class="section-head" style="top:1184px">HOW CAN WE HELP YOU?</div>

  <div class="card" style="left:48px;top:1326px">
    <div class="card-img" role="img" aria-label="White baseboard heater along a wall" style="background:linear-gradient(135deg,#f3efe6,#d9c38f)"></div>
    <div class="card-cap on">BASEBOARD HEAT REPLACEMENT</div>
  </div>
  <div class="card" style="left:429px;top:1326px">
    <div class="card-img" role="img" aria-label="Ductless unit above a sofa on a stone wall" style="background:linear-gradient(180deg,#8a8a8a,#cfcfcf)"></div>
    <div class="card-cap">DUCTLESS FOR ADDITIONS &amp; REMODELS</div>
  </div>
  <div class="card" style="left:808px;top:1326px">
    <div class="card-img" role="img" aria-label="Hand holding a remote control below a wall unit" style="background:linear-gradient(135deg,#e9eef2,#b9c3cb)"></div>
    <div class="card-cap">DUCTLESS WARRANTY</div>
  </div>

  <div class="card" style="left:48px;top:1781px">
    <div class="card-img" role="img" aria-label="Technician fitting an indoor ductless unit" style="background:linear-gradient(135deg,#f1f1f1,#8ea6c8)"></div>
    <div class="card-cap">DUCTLESS INSTALLATION</div>
  </div>
  <div class="card" style="left:429px;top:1781px">
    <div class="card-img" role="img" aria-label="Technician repairing an open ductless unit" style="background:linear-gradient(135deg,#d8dde2,#5a78a8)"></div>
    <div class="card-cap">DUCTLESS REPAIRS</div>
  </div>
  <div class="card" style="left:808px;top:1781px">
    <div class="card-img" role="img" aria-label="Person relaxing on a sofa in a cooled living room" style="background:linear-gradient(135deg,#e4e8ec,#a89f93)"></div>
    <div class="card-cap">WHOLE HOUSE DUCTLESS</div>
  </div>

  <!-- Contact / why / testimonial / quality -->
  <svg class="abs" style="left:0;top:2280px" width="1200" height="1460" aria-hidden="true">
    <rect x="0" y="0" width="1200" height="1460" fill="#e4e4e4"/>
    <polygon points="0,133 684,13 684,752 0,937" fill="#ffe000"/>
    <polygon points="684,808 1200,660 1200,1420 684,1428" fill="#ffe000"/>
  </svg>

  <div class="abs block-title" style="left:48px;top:2475px">CONTACT US TODAY</div>
  <div class="h-line" style="left:48px;top:2512px;width:236px;background:var(--ink);height:3px"></div>
  <div class="abs" style="left:48px;top:2549px;font-size:16px;line-height:19px;color:var(--ink)">ILL OUT THE FORM BELOW<br>OR CALL CASCADE DUCTLESS CREW AT</div>
  <div class="abs" style="left:48px;top:2594px;font-weight:900;font-size:27px;color:var(--ink)">500-555-0182</div>

  <div class="field" style="left:48px;top:2664px;width:263px;height:49px">Name</div>
  <div class="field" style="left:364px;top:2664px;width:263px;height:49px">Last Name</div>
  <div class="field" style="left:48px;top:2727px;width:263px;height:49px">Phone</div>
  <div class="field" style="left:364px;top:2727px;width:263px;height:49px">Mail</div>
  <div class="field" style="left:48px;top:2792px;width:579px;height:49px">Are You New Customer ?</div>
  <div class="field" style="left:48px;top:2857px;width:579px;height:150px">Message</div>
  <div class="btn-dark" style="left:187px;top:3034px;width:301px;height:50px;line-height:50px;font-size:17px;border-radius:25px">Send Information</div>

  <div class="abs block-title" style="left:736px;top:2405px">WHY CHOOSE<br>CASCADE DUCTLESS CREW?</div>
  <div class="h-line" style="left:736px;top:2479px;width:189px"></div>

  <div class="why-item" style="top:2561px;height:80px">
    <svg width="74" height="74" viewBox="0 0 74 74" aria-hidden="true">
      <rect x="4" y="8" width="46" height="60" fill="#ffe000" stroke="#111" stroke-width="3"/>
      <line x1="12" y1="22" x2="42" y2="22" stroke="#111" stroke-width="3"/>
      <line x1="12" y1="32" x2="42" y2="32" stroke="#111" stroke-width="3"/>
      <circle cx="22" cy="52" r="9" fill="none" stroke="#111" stroke-width="3"/>
      <polyline points="17,52 21,56 28,47" fill="none" stroke="#111" stroke-width="3"/>
      <line x1="66" y1="10" x2="46" y2="50" stroke="#111" stroke-width="4"/>
    </svg>
    <div class="why-text" style="top:32px">PROVIDING OPTIONS TO OUR CUSTOMERS<br>WHERE IT MATTERS MOST. OFFER APPLIES<br>TO TARLEN SYSTEMS.</div>
  </div>
  <div class="why-item" style="top:2688px;height:80px">
    <svg width="74" height="74" viewBox="0 0 74 74" aria-hidden="true">
      <polygon points="37,4 66,16 62,46 37,68 12,46 8,16" fill="#ffe000" stroke="#111" stroke-width="3"/>
      <polyline points="24,36 33,45 51,26" fill="none" stroke="#111" stroke-width="5"/>
    </svg>
    <div class="why-text" style="top:8px"><b>365 DAY, MONEY BACK GUARANTEE</b>WE HAVE INTEGRITY, AND STAND BEHIND OUR<br>SERVICES TO ENSURE THAT YOU ARE SATISFIED.</div>
  </div>
  <div class="why-item" style="top:2828px;height:90px">
    <svg width="74" height="80" viewBox="0 0 74 80" aria-hidden="true">
      <circle cx="37" cy="34" r="18" fill="#ffe000" stroke="#111" stroke-width="3"/>
      <path d="M13 36 A24 24 0 0 1 61 36" fill="none" stroke="#111" stroke-width="4"/>
      <rect x="8" y="32" width="9" height="16" fill="#111"/>
      <rect x="57" y="32" width="9" height="16" fill="#111"/>
      <path d="M10 78 Q37 50 64 78" fill="#ffe000" stroke="#111" stroke-width="3"/>
    </svg>
    <div class="why-text" style="top:6px"><b>WE ARE THE EXPERTS IN DUCTLESS<br>SERVICES</b>NOT ONLY CAN WE PERFORM THE SERVICES WITH<br>PRECISION, BUT WE CAN ALSO EDUCATE YOU ON<br>WHY DUCTLESS IS THE WAY TO DO.</div>
  </div>

  <div class="abs" style="left:740px;top:3134px;font-weight:900;font-size:26px;line-height:34px;color:var(--ink)">Oh, my gosh! These guys are<br>awesome.</div>
  <div class="quote-mark" style="left:730px;top:3228px">&ldquo;</div>
  <div class="quote-mark" style="left:1024px;top:3422px">&rdquo;</div>
  <div class="abs" style="left:736px;top:3363px;width:420px;font-size:15px;line-height:23px;color:var(--ink)">"They do good work, use good products, and the incentives are great! We liked the first one so much, we got a second system in the second side of a duplex."</div>
  <div class="abs" style="left:736px;top:3490px;font-size:15px;color:var(--ink)">- Dana M.</div>
  <svg class="abs" style="left:734px;top:3572px" width="130" height="32" aria-hidden="true">
    <polyline points="16,4 6,16 16,28" fill="none" stroke="#111" stroke-width="4"/>
    <polyline points="114,4 124,16 114,28" fill="none" stroke="#111" stroke-width="4"/>
    <text x="65" y="25" text-anchor="middle" font-family="Lato, sans-serif" font-weight="900" font-size="24" fill="#111">1-5</text>
  </svg>

  <div class="abs" style="left:48px;top:3292px;font-weight:900;font-size:27px;color:var(--ink)">Quality Work Guarantee</div>
  <div class="h-line" style="left:48px;top:3337px;width:178px"></div>
  <div class="abs" style="left:48px;top:3370px;width:585px;font-size:16.5px;line-height:23.3px;color:var(--ink)">At Cascade Ductless Crew, we take great pride in our work. As the only heating and cooling company in the area that specializes in ductless systems, our expert technicians provide only the highest level of service every time. We have the resources and the training as a Kenrow Elite Dealer and Hollis Premier Contractor to get the job done. Trust us to deliver total home comfort with our high-performing, energy-efficient ductless heat pumps or air conditioners and superior workmanship.</div>

  <!-- More services -->
  <div class="abs" style="left:0;top:3740px;width:1200px;height:648px;background:var(--white)"></div>
  <div class="abs" style="left:48px;top:3833px;font-weight:900;font-size:28px;color:var(--ink)">We Stand Behind Our Ductless Services</div>
  <div class="abs" style="left:48px;top:3879px;font-size:17px;color:var(--ink)">See Other Ways We Can Help with Your Ductless System</div>
  <div class="h-line" style="left:48px;top:3914px;width:290px"></div>

  <div class="more-card" style="left:48px;top:3988px">
    <div class="more-img" role="img" aria-label="Person on a sofa pointing a remote at a wall unit" style="background:linear-gradient(180deg,#f0f0f0,#6d7580)"></div>
    <div class="more-body" style="background:var(--yellow)">
      <div class="more-title" style="color:var(--ink)">Get Some Answers</div>
      <div class="more-btn" style="background:var(--ink);color:var(--white)">DUCTLESS FAQ</div>
    </div>
  </div>
  <div class="more-card" style="left:425px;top:3988px">
    <div class="more-img" role="img" aria-label="Stack of coins on banknotes" style="background:linear-gradient(135deg,#6b6356,#c9bda6)"></div>
    <div class="more-body" style="background:var(--card-gray)">
      <div class="more-title" style="color:var(--yellow)">Our Financing Options</div>
      <div class="more-btn" style="background:var(--yellow);color:var(--ink)">FINANCING</div>
    </div>
  </div>
  <div class="more-card" style="left:806px;top:3988px">
    <div class="more-img" role="img" aria-label="Wall unit blowing cool air in a bright room" style="background:linear-gradient(135deg,#f2f4f6,#7fb2dd)"></div>
    <div class="more-body" style="background:var(--card-gray)">
      <div class="more-title" style="color:var(--yellow)">Stay Up To Date</div>
      <div class="more-btn" style="background:var(--yellow);color:var(--ink)">OUR BLOG</div>
    </div>
  </div>

  <!-- Footer -->
  <footer class="footer">
    <div class="abs" style="left:100px;top:48px;display:flex;align-items:center;gap:10px">
      <div style="width:26px;height:26px;border-radius:50%;background:var(--yellow)"></div>
      <div style="font-weight:900;font-size:20px;color:var(--yellow)">Amber Kite Services</div>
    </div>
    <div class="abs" style="left:104px;top:84px;font-weight:900;font-size:15px;color:var(--yellow)">DUCTLESS EXPERTS</div>
    <div class="abs" style="left:0;width:372px;text-align:center;top:132px;font-weight:900;font-size:36px">500-555-0182</div>
    <div class="abs" style="left:0;width:372px;text-align:center;top:186px;font-size:22px">Follow Us</div>

    <div class="foot-title" style="left:400px;top:42px">Cascade Ductless Location</div>
    <div class="foot-addr" style="left:400px;top:80px">2210 SE Alder Park Way,<br>Suite B12<br>Riverton, OR 97000</div>
    <div class="map" style="left:403px;top:153px;width:218px;height:152px" role="img" aria-label="Street map around the Riverton location"></div>

    <div class="foot-title" style="left:738px;top:42px">A Division of Summit Air Heating</div>
    <div class="foot-addr" style="left:738px;top:84px">8840 SW Larch Ave. Fernridge,<br>OR 97001</div>
    <div class="map" style="left:740px;top:146px;width:220px;height:159px" role="img" aria-label="Street map around the Fernridge office"></div>

    <div class="foot-title" style="right:48px;top:44px">Quick Link</div>
    <div class="quick" style="top:90px">Home</div>
    <div class="quick" style="top:123px">About us</div>
    <div class="quick" style="top:154px">Ductless Heat Pumps</div>
    <div class="quick" style="top:188px">Ductless Heat Pumps FAQ</div>
    <div class="quick" style="top:223px">Reviews</div>
    <div class="quick" style="top:254px">Financing</div>
    <div class="quick" style="top:291px">Contact us</div>

    <div class="foot-strip"></div>
  </footer>
  <div class="social" style="left:100px"></div>
  <div class="social" style="left:165px"></div>
  <div class="social" style="left:228px"></div>

</div>
</body>
</html>
```